Revamp Landing Page

Our current landing page is http://velvetdenkx.com/ and we're looking for our site to look like this http://www.goldparrotclub.com/. Classy, Sleek, Simple elegant.

The site should be desktop and mobile optimized.
Pages should be built out and the same structure. Drink Menu, Gallery, Events, Table Reservations, Membership, Press, Contact Us.

Feel free to use the images on our website.

```html
<!DOCTYPE html>
<html lang="en">
<head>
<meta charset="utf-8">
<title>Velvet Den — Landing Page</title>
<link rel="stylesheet" href="https://fonts.googleapis.com/css2?family=Josefin+Sans:wght@300;400;600&display=swap">
<style>
  :root {
    --navy: #08213a;
    --navy-deep: #051a2f;
    --gold: #8c7a3e;
    --white: #ffffff;
    --text-soft: #e6e9ee;
    --page-bg: #ffffff;
    --photo-warm: #6b4a26;
    --photo-dark: #1c120b;
  }
  * { margin: 0; padding: 0; box-sizing: border-box; }
  html, body { width: 1200px; height: 526px; overflow: hidden; background: var(--page-bg); }
  body { position: relative; font-family: "Josefin Sans", sans-serif; color: var(--white); }

  .desktop { position: absolute; left: 0; top: 0; width: 822px; height: 526px; background: var(--navy); }
  .mobile { position: absolute; left: 905px; top: 77px; width: 223px; height: 393px; background: var(--navy); }

  .brand { position: absolute; font-weight: 300; color: var(--white); letter-spacing: 1px; white-space: nowrap; }
  .desktop .brand { left: 419px; top: 24px; transform: translateX(-50%); font-size: 22px; }
  .mobile .brand { left: 28px; top: 28px; font-size: 13px; }

  .main-nav { position: absolute; top: 62px; left: 0; width: 822px; height: 14px; }
  .main-nav a { position: absolute; top: 0; transform: translateX(-50%); font-size: 9.5px; line-height: 14px; color: var(--white); text-decoration: none; white-space: nowrap; text-transform: uppercase; }
  .main-nav a.is-active { background: var(--gold); padding: 1px 6px 0; border-radius: 3px; line-height: 13px; }

  .hero { position: absolute; overflow: hidden; }
  .desktop .hero { left: 73px; top: 93px; width: 677px; height: 385px; }
  .mobile .hero { left: 29px; top: 65px; width: 165px; height: 260px; }
  .hero-photo { position: absolute; inset: 0;
    background: radial-gradient(ellipse at 50% 30%, #a57a40 0%, var(--photo-warm) 30%, #3a2714 60%, var(--photo-dark) 100%); }
  .hero-copy { position: absolute; left: 0; right: 0; text-align: center; }
  .desktop .hero-copy { top: 180px; }
  .mobile .hero-copy { top: 101px; }
  .hero-title { font-weight: 300; text-transform: uppercase; }
  .desktop .hero-title { font-size: 20px; line-height: 22px; }
  .mobile .hero-title { font-size: 10px; line-height: 12px; }
  .hero-tagline { text-transform: uppercase; font-weight: 400; }
  .desktop .hero-tagline { font-size: 7.5px; margin-top: 5px; }
  .mobile .hero-tagline { font-size: 4.5px; margin-top: 2px; white-space: nowrap; }
  .btn-more { display: inline-block; background: var(--gold); color: var(--white); border-radius: 4px; text-decoration: none; }
  .desktop .btn-more { width: 72px; height: 14px; font-size: 7.5px; line-height: 15px; margin-top: 7px; }
  .mobile .btn-more { width: 72px; height: 16px; font-size: 7.5px; line-height: 17px; margin-top: 7px; }

  .slide-dots { position: absolute; }
  .desktop .slide-dots { left: 27px; top: 243px; }
  .mobile .slide-dots { left: 10px; top: 173px; }

  .copyright { position: absolute; color: var(--text-soft); white-space: nowrap; }
  .desktop .copyright { left: 73px; top: 497px; font-size: 11px; }
  .mobile .copyright { left: 0; right: 0; top: 341px; text-align: center; font-size: 7.5px; }

  .social { position: absolute; }
  .desktop .social { left: 618px; top: 495px; }
  .mobile .social { left: 47px; top: 366px; }

  .menu-toggle { position: absolute; left: 178px; top: 28px; }
</style>
</head>
<body>

<section class="desktop" aria-label="Desktop landing page">
  <div class="brand">VELVET DEN</div>
  <nav class="main-nav">
    <a class="is-active" href="#" style="left:108px">Drink Menu</a>
    <a href="#" style="left:207px">Gallery</a>
    <a href="#" style="left:294px">Events</a>
    <a href="#" style="left:409px">Table Reservations</a>
    <a href="#" style="left:534px">Membership</a>
    <a href="#" style="left:626px">Press</a>
    <a href="#" style="left:720px">Contact Us</a>
  </nav>

  <svg class="slide-dots" width="12" height="42" viewBox="0 0 12 42" aria-hidden="true">
    <circle cx="6" cy="5" r="2.3" fill="#fff"/>
    <circle cx="6" cy="15" r="2.3" fill="#fff"/>
    <circle cx="6" cy="26" r="3.8" fill="none" stroke="#fff" stroke-width="1.3"/>
    <circle cx="6" cy="37" r="2.3" fill="#fff"/>
  </svg>

  <div class="hero">
    <div class="hero-photo" role="img" aria-label="Warmly lit bar interior with backlit bottle shelves, bar stools and lounge tables"></div>
    <div class="hero-copy">
      <h1 class="hero-title">Velvet Den</h1>
      <p class="hero-tagline">A home away from home for the local community</p>
      <a class="btn-more" href="#">Read More</a>
    </div>
  </div>

  <p class="copyright">© 2018 Velvet Den. All Rights Reserved.</p>
  <svg class="social" width="142" height="22" viewBox="0 0 142 22" aria-label="Social links">
    <g fill="none" stroke="#fff" stroke-width="1.2">
      <circle cx="11" cy="11" r="9.5"/>
      <circle cx="38" cy="11" r="9.5"/>
      <circle cx="66" cy="11" r="9.5"/>
      <circle cx="93" cy="11" r="9.5"/>
      <circle cx="122" cy="11" r="9.5"/>
    </g>
  </svg>
</section>

<section class="mobile" aria-label="Mobile landing page">
  <div class="brand">VELVET DEN</div>
  <svg class="menu-toggle" width="15" height="12" viewBox="0 0 15 12" aria-label="Menu">
    <g fill="#fff"><rect y="0" width="15" height="2"/><rect y="5" width="15" height="2"/><rect y="10" width="15" height="2"/></g>
  </svg>

  <svg class="slide-dots" width="10" height="30" viewBox="0 0 10 30" aria-hidden="true">
    <circle cx="5" cy="3" r="1.8" fill="#fff"/>
    <circle cx="5" cy="10" r="1.8" fill="#fff"/>
    <circle cx="5" cy="18" r="2.8" fill="none" stroke="#fff" stroke-width="1"/>
    <circle cx="5" cy="27" r="1.8" fill="#fff"/>
  </svg>

  <div class="hero">
    <div class="hero-photo" role="img" aria-label="Warmly lit bar interior with backlit bottle shelves and bar stools"></div>
    <div class="hero-copy">
      <h2 class="hero-title">Velvet Den</h2>
      <p class="hero-tagline">A home away from home for the local community</p>
      <a class="btn-more" href="#">Read More</a>
    </div>
  </div>

  <p class="copyright">© 2018 Velvet Den. All Rights Reserved.</p>
  <svg class="social" width="130" height="20" viewBox="0 0 130 20" aria-label="Social links">
    <g fill="none" stroke="#fff" stroke-width="1">
      <circle cx="9" cy="10" r="8.5"/>
      <circle cx="37" cy="10" r="8.5"/>
      <circle cx="65" cy="10" r="8.5"/>
      <circle cx="92" cy="10" r="8.5"/>
      <circle cx="120" cy="10" r="8.5"/>
    </g>
  </svg>
</section>

</body>
</html>
```